Business Card Design Project

We have a logo, but would like to expand the use of it into a business card design. We are a B2B technology exchange platform for institutional investors to invest excess cash into short term assets matching their credit and pricing parameters. The assets are fractionalized and investors invest in portions.

Our customers are large, institutional, financial companies who are a bit traditional. We are high energy rebels with a cause...we are a disruptive technology and want to be viewed as a game changer but we need to present an image of trustworthiness and secure.

We are open not only to the image design but the material, die cut, etc. but want to stay in the traditional size of a business card.

We have other formats of the logo if needed. Our website is www.brambleharbor.com
Updates

I have posted a powerpoint template that we have been using.  This should not be considered the template we will use (after business cards we will have another project to incorporate business card design into powerpoint template) but just to give you a flavor of where we have been and have used in the past.

Target Market(s)

Institutional investors, asset managers, large fund institutions

Industry/Entity Type

Financial

Requirements
Must have
• Our logo
Traditional size
Nice to have
• unique use of logo, unique material, die cut, etc
Crisp, clean look
Use of both sides of card in a creative manner

```html
<!DOCTYPE html>
<html lang="en">
<head>
<meta charset="utf-8">
<title>Bramble Harbor Business Cards</title>
<link href="https://fonts.googleapis.com/css2?family=Arimo:wght@400;700&display=swap" rel="stylesheet">
<style>
  :root {
    --canvas: #e6e7e8;
    --paper: #ffffff;
    --paper-soft: #f4f4f4;
    --orange: #f7982f;
    --peach: #fbc99a;
    --slate: #6b6c6e;
    --ink: #444446;
    --line: #2a2a2a;
  }
  html, body {
    margin: 0;
    padding: 0;
    width: 1200px;
    height: 1112px;
    overflow: hidden;
    background: var(--canvas);
    font-family: "Arimo", Arial, sans-serif;
  }
  .sheet { position: relative; width: 1200px; height: 1112px; }
  .card {
    position: absolute;
    width: 524px;
    height: 300px;
    background: var(--paper);
    border-radius: 80px 0 76px 0;
    overflow: hidden;
  }
  .card--soft { background: var(--paper-soft); }
  .card svg.art { position: absolute; left: 0; top: 0; width: 524px; height: 302px; }
  .brand {
    position: absolute;
    display: flex;
    align-items: center;
    gap: 6px;
    color: var(--slate);
    font-weight: 700;
    white-space: nowrap;
    letter-spacing: 0.02em;
    line-height: 1.15;
  }
  .brand__dot { border-radius: 50%; background: var(--orange); display: inline-block; flex: none; }
  .brand--small { font-size: 19px; }
  .brand--small .brand__dot { width: 12px; height: 12px; }
  .brand--large { font-size: 36px; left: 60px; top: 141px; gap: 8px; }
  .brand--large .brand__dot { width: 26px; height: 26px; }
  .contact {
    position: absolute;
    left: 37px;
    color: var(--ink);
    font-size: 12.5px;
    line-height: 16.8px;
    margin: 0;
  }
  .contact--web { top: 225px; }
  .strip {
    position: absolute;
    font-size: 9.5px;
    font-weight: 700;
    white-space: nowrap;
  }
  .strip--orange { color: var(--orange); }
  .strip--ink { color: var(--ink); }
</style>
</head>
<body>
<div class="sheet">

  <!-- Row 1 front -->
  <div class="card" style="left:48px;top:40px;">
    <svg class="art" viewBox="0 0 524 302" aria-hidden="true">
      <circle cx="450" cy="215" r="92" fill="var(--orange)"/>
    </svg>
    <div class="brand brand--small" style="left:168px;top:24px;">BRAMBLE HARBOR<span class="brand__dot"></span></div>
    <p class="contact" style="top:94px;">Bramble Harbor, Inc<br>2318 Fernhill Crest Road<br>Suite 410<br>Alder Springs, CA 90417<br>P 555.204.7718</p>
    <p class="contact contact--web">Marketing@BrambleHarbor.com<br>www.brambleharbor.com</p>
  </div>

  <!-- Row 1 back -->
  <div class="card" style="left:620px;top:30px;height:302px;">
    <svg class="art" viewBox="0 0 524 302" aria-hidden="true">
      <path d="M0,100 C40,210 150,285 420,302 L0,302 Z" fill="var(--orange)"/>
    </svg>
    <div class="brand brand--large">BRAMBLE HARBOR<span class="brand__dot"></span></div>
  </div>

  <!-- Row 2 front -->
  <div class="card card--soft" style="left:58px;top:384px;">
    <svg class="art" viewBox="0 0 524 302" aria-hidden="true">
      <circle cx="450" cy="215" r="96" fill="var(--paper)"/>
      <circle cx="450" cy="215" r="90" fill="var(--orange)"/>
    </svg>
    <div class="brand brand--small" style="left:168px;top:22px;">BRAMBLE HARBOR<span class="brand__dot"></span></div>
    <p class="contact" style="top:92px;">Bramble Harbor, Inc<br>2318 Fernhill Crest Road<br>Suite 410<br>Alder Springs, CA 90417<br>P 555.204.7718</p>
    <p class="contact contact--web">Marketing@BrambleHarbor.com<br>www.brambleharbor.com</p>
  </div>

  <!-- Row 2 back -->
  <div class="card card--soft" style="left:607px;top:378px;">
    <svg class="art" viewBox="0 0 524 302" aria-hidden="true">
      <path d="M0,100 C40,210 150,285 420,302 L0,302 Z" fill="var(--slate)"/>
    </svg>
    <div class="brand brand--large">BRAMBLE HARBOR<span class="brand__dot"></span></div>
  </div>

  <!-- Row 3 front -->
  <div class="card" style="left:38px;top:768px;">
    <svg class="art" viewBox="0 0 524 302" aria-hidden="true">
      <circle cx="435" cy="170" r="98" fill="var(--peach)"/>
    </svg>
    <div class="brand" style="left:18px;top:118px;font-size:24px;">BRAMBLE HARBOR<span class="brand__dot" style="width:16px;height:16px;"></span></div>
    <div class="strip strip--orange" style="left:10px;top:243px;">Marketing@BrambleHarbor.com</div>
    <div class="strip strip--orange" style="left:195px;top:243px;">www.brambleharbor.com</div>
    <div class="strip strip--ink" style="left:10px;top:263px;">Bramble Harbor, Inc, 2318 Fernhill Crest Road, Suite 410, Alder Springs, CA 90417, P 555.204.7718</div>
  </div>

  <!-- Row 3 back -->
  <div class="card" style="left:588px;top:760px;">
    <svg class="art" viewBox="0 0 524 302" aria-hidden="true">
      <path d="M0,100 C40,210 150,285 420,302 L0,302 Z" fill="var(--slate)"/>
      <line x1="60" y1="6" x2="150" y2="56" stroke="var(--line)" stroke-width="1.2"/>
      <line x1="30" y1="22" x2="95" y2="58" stroke="var(--orange)" stroke-width="1.2"/>
      <line x1="10" y1="46" x2="40" y2="62" stroke="var(--line)" stroke-width="1.2"/>
      <line x1="276" y1="208" x2="420" y2="290" stroke="var(--line)" stroke-width="1.2"/>
      <line x1="328" y1="204" x2="472" y2="290" stroke="var(--orange)" stroke-width="1.2"/>
      <line x1="388" y1="204" x2="500" y2="270" stroke="var(--line)" stroke-width="1.2"/>
    </svg>
    <div class="brand brand--large">BRAMBLE HARBOR<span class="brand__dot"></span></div>
  </div>

</div>
</body>
</html>
```